Web Design for a Biotech Consulting Firm

We need a web site design for a new business based in Philadelphia called Corventa Dx. This is a consulting firm that will serve medical diagnostics industry, which is part of the life science/healthcare industry focusing on developing and marketing products that help in early detection, monitoring or management of diseases. Our consulting firm will help medical diagnostic companies to overcome key challenges in designing, evaluating and marketing new products.Our company name is Corventa Dx. Corventa is Latin word for "something" Dx represents diagnostics. The idea behind the name is that we help companies to transform the original, early product ideas ("nothing") into "something"; which is a product with full clinical utility that will help to improve health and well-being.The web site should use the visual feel of the logo (attached), be modern, simple and clean looking and represent creativity, innovation, scientific thinking and progress.
Updates

Wix Design is acceptable

Industry/Entity Type

Biotechnology

Coding

Coded - Design and coding required

Number of Pages Required

1 page

Font styles to use
Sans Serif

Requirements
Must have
• simple, clean look couple of pages
Should not have
• a lot of pages

```html
<!DOCTYPE html>
<html lang="en">
<head>
<meta charset="utf-8">
<title>Corventa Dx — Consulting for Medical Diagnostics</title>
<link href="https://fonts.googleapis.com/css2?family=Montserrat:wght@500;600;700&family=Jost:wght@400;500&family=Oswald:wght@500;600&family=Roboto+Condensed:wght@400&family=Roboto:wght@400&display=swap" rel="stylesheet">
<style>
:root{
  --blue:#1a84f5;
  --blue-soft:#a9cdf7;
  --ink:#1b1b1b;
  --text:#3a3a3a;
  --muted:#5a5a5a;
  --pale:#f3f7fd;
  --line:#e3e8ef;
  --white:#ffffff;
}
*{margin:0;padding:0;box-sizing:border-box}
html,body{width:1200px;height:3280px;overflow:hidden}
body{position:relative;background:var(--white);font-family:"Jost",sans-serif;color:var(--text)}

/* header */
.site-header{position:absolute;left:0;top:0;width:1200px;height:113px;background:var(--white)}
.brand{position:absolute;left:113px;top:38px}
.brand-name{font-family:"Montserrat",sans-serif;font-weight:500;font-size:17px;color:var(--ink);white-space:nowrap}
.main-nav{position:absolute;top:47px;left:629px}
.main-nav a{position:absolute;font-family:"Montserrat",sans-serif;font-weight:600;font-size:13px;color:var(--ink);text-decoration:none;white-space:nowrap}
.main-nav a.active{color:var(--blue)}

/* hero */
.hero{position:absolute;left:0;top:113px;width:1200px;height:549px;background:linear-gradient(90deg,#e6e6e8 0%,#e0e1e4 35%,#cfd3d8 55%,#b9c2cc 75%,#c9cfd6 100%)}
.hero-kicker{position:absolute;left:114px;top:234px;font-family:"Oswald",sans-serif;font-weight:500;font-size:26px;color:var(--ink);letter-spacing:-.3px}
.hero-title{position:absolute;left:113px;top:268px;font-family:"Oswald",sans-serif;font-weight:600;font-size:44px;color:var(--blue);letter-spacing:-.3px}
.dots{position:absolute;left:115px;top:354px;display:flex;gap:6px}
.dots span{width:12px;height:12px;border-radius:50%;border:1px solid #555}
.dots span.on{background:var(--blue);border-color:var(--blue)}

/* about */
.about{position:absolute;left:0;top:662px;width:1200px;height:575px;background:var(--pale)}
.about-frame{position:absolute;left:113px;top:90px;width:373px;height:390px;border:4px solid var(--blue-soft)}
.about-photo{position:absolute;left:144px;top:119px;width:375px;height:334px;background:linear-gradient(100deg,#9aa2ab 0%,#d9dde1 40%,#eef0f2 60%,#c7ccd1 100%)}
.section-title{font-family:"Montserrat",sans-serif;font-weight:600;font-size:30px;color:var(--ink)}
.section-title em{font-style:normal;color:var(--blue)}
.about-title{position:absolute;left:569px;top:136px}
.about-lead{position:absolute;left:569px;top:182px;width:525px;font-size:15.5px;line-height:22px;color:var(--ink)}
.about-body{position:absolute;left:569px;top:231px;width:520px;font-size:13.6px;line-height:23px;color:var(--muted)}
.btn-outline{position:absolute;display:flex;align-items:center;justify-content:center;border:2px solid var(--blue);font-family:"Roboto Condensed",sans-serif;font-size:13px;color:var(--ink);text-decoration:none;background:transparent}

/* services */
.services-title{position:absolute;left:0;width:1200px;top:1315px;text-align:center}
.service-card{position:absolute;top:1385px;width:305px;height:276px;background:var(--white);box-shadow:0 0 8px rgba(30,60,110,.1);padding:26px 18px 0 18px}
.service-icon{display:block;width:62px;height:62px}
.service-card h3{margin-top:21px;font-family:"Montserrat",sans-serif;font-weight:600;font-size:16px;color:var(--ink)}
.service-card p{margin-top:10px;font-size:13.8px;line-height:20.5px;color:var(--muted)}
.more-link{display:inline-flex;align-items:center;gap:6px;font-family:"Roboto Condensed",sans-serif;font-size:13px;color:var(--ink);text-decoration:none}
.more-link .arrow{width:16px;height:10px;flex:none}
.service-card .more-link{margin-top:18px}

/* feature band */
.feature-photo{position:absolute;left:0;top:1755px;width:1200px;height:504px;background:linear-gradient(90deg,#e9eef3 0%,#c9d6e2 30%,#dfe7ee 55%,#c5d4e1 80%,#eef2f5 100%)}
.feature-box{position:absolute;left:113px;top:1871px;width:419px;height:445px;background:var(--blue);padding:52px 24px 0 24px;color:var(--white)}
.feature-box h2{font-family:"Montserrat",sans-serif;font-weight:600;font-size:27.5px;line-height:39px;color:var(--white);letter-spacing:-.2px}
.feature-box p{margin-top:18px;font-size:16px;line-height:25.5px;color:#eaf3ff}
.feature-box .more-link{margin-top:35px;color:var(--white)}

/* news */
.news-title{position:absolute;left:0;width:1200px;top:2394px;text-align:center}
.news-card{position:absolute;top:2465px;width:305px;height:338px;background:var(--white);border:1px solid var(--line);padding:6px}
.news-img{width:291px;height:237px}
.news-date{margin:20px 0 0 11px;font-family:"Roboto",sans-serif;font-size:11px;color:var(--blue)}
.news-card h3{margin:6px 0 0 11px;font-family:"Montserrat",sans-serif;font-weight:600;font-size:14px;line-height:20px;color:var(--ink)}

/* footer */
.site-footer{position:absolute;left:0;top:2969px;width:1200px;height:311px;background:var(--pale)}
.footer-heading{position:absolute;top:56px;font-family:"Montserrat",sans-serif;font-weight:600;font-size:14px;color:var(--blue)}
.quick-links{position:absolute;left:113px;top:85px;list-style:none}
.quick-links li{height:27px;font-size:14px;color:var(--ink)}
.quick-links li::before{content:"»";color:#888;margin-right:10px;font-size:12px}
.contact{position:absolute;left:304px;top:85px;font-size:13.5px;color:var(--ink)}
.contact-row{display:flex;gap:8px;position:absolute;left:0;white-space:nowrap}
.contact-row svg{width:13px;height:15px;flex:none;margin-top:2px}
.contact strong{font-family:"Montserrat",sans-serif;font-weight:600;font-size:13px}
.map{position:absolute;left:620px;top:91px;width:243px;height:114px;background:linear-gradient(135deg,#f3eedf,#e8e4d4 50%,#f1ecdd);border:1px solid #e2ddcd}
.footer-brand{position:absolute;left:960px;top:125px}
.footer-brand .brand-name{font-size:22px}
.footer-rule{position:absolute;left:113px;top:267px;width:974px;height:1px;background:#cfd6df}
.copyright{position:absolute;left:113px;top:279px;font-size:13px;color:var(--ink)}
.social{position:absolute;left:973px;top:276px;display:flex;gap:7px}
.social span{width:23px;height:23px}
</style>
</head>
<body>

<header class="site-header">
  <div class="brand"><span class="brand-name">Corventa Dx</span></div>
  <nav class="main-nav">
    <a class="active" style="left:0">HOME</a>
    <a style="left:82px">ABOUT US</a>
    <a style="left:191px">SERVIES</a>
    <a style="left:289px">NEWS</a>
    <a style="left:372px">CONTACT US</a>
  </nav>
</header>

<section class="hero" role="img" aria-label="Photo of a doctor in a white coat consulting with an older patient at a desk">
  <p class="hero-kicker">CONSULTING FIRM SERVING MEDICAL</p>
  <h1 class="hero-title">DIAGNOSTICS INDUSTRY</h1>
  <div class="dots"><span></span><span class="on"></span><span></span></div>
</section>

<section class="about">
  <div class="about-frame"></div>
  <div class="about-photo" role="img" aria-label="Photo of a businessman shaking hands with a doctor in a hospital corridor"></div>
  <h2 class="section-title about-title">ABOUT <em>CORVENTA DX</em></h2>
  <p class="about-lead">Lorem ipsum dolor sit amet, consectetuer adipiscing elit, sed diam nonummy nibh euismod tincidunt ut laoreet dolore magna.</p>
  <p class="about-body">Lorem ipsum dolor sit amet, consectetuer adipiscing elit, sed diam nonummy nibh mod tincidunt ut laoreet dolore magna aliquam erat volutpat. Ut wisi enim ad minim venim, quis nostrud exerci tation ullaorper suscpit lobortis nisl ut aliquip ex ea comodo consat. Duis autem vel eum iriure dolor in hendrerit in vulputate velit esse molestie consequat, vel illum dolore eu feugiat nulla facilisis at vero eros et accumsan et iusto odio dignissim qui blandit praesent luptatum zzril delenit augue duis facilisi.</p>
  <a class="btn-outline" style="left:569px;top:388px;width:113px;height:41px">READ MORE</a>
</section>

<h2 class="section-title services-title">OUR <em>SERVICES</em></h2>

<article class="service-card" style="left:113px">
  <svg class="service-icon" viewBox="0 0 62 62" fill="none" stroke="#1a84f5" stroke-width="2.2" stroke-linejoin="round">
    <rect x="2" y="3" width="58" height="42" rx="2"/><line x1="2" y1="37" x2="60" y2="37"/>
    <path d="M24 45v8h14v-8M16 57h30"/>
    <path d="M12 33V17l4-6 4 6v16z"/><path d="M26 33V12h8v21z"/><line x1="26" y1="18" x2="30" y2="18"/><line x1="26" y1="24" x2="30" y2="24"/>
    <path d="M40 33V19h5v14zM49 33V9h6v24z"/>
  </svg>
  <h3>DESIGNING</h3>
  <p>Lorem ipsum dolor sit consectetuer adipiscing elit sed diam nonumy nibh euismod tincidunt ut laoreet dolore magna.Ut wisi enim minim venim quis nostrud exerci.</p>
  <a class="more-link">READ MORE <svg class="arrow" viewBox="0 0 16 10"><path d="M0 5h13M9 1l4 4-4 4" stroke="#1b1b1b" stroke-width="2" fill="none"/></svg></a>
</article>

<article class="service-card" style="left:448px">
  <svg class="service-icon" viewBox="0 0 62 62" fill="none" stroke="#1a84f5" stroke-width="2.2" stroke-linejoin="round">
    <rect x="4" y="6" width="40" height="54" rx="2"/><rect x="16" y="2" width="16" height="8" rx="1"/>
    <rect x="11" y="17" width="6" height="6"/><rect x="11" y="30" width="6" height="6"/><rect x="11" y="43" width="6" height="6"/>
    <path d="M21 19l3 3 5-5M21 33l3 3 5-5M21 43l6 6M27 43l-6 6"/>
    <path d="M56 12l4 4-18 24-6 2 2-6z"/>
  </svg>
  <h3>EVALUATING</h3>
  <p>Lorem ipsum dolor sit consectetuer adipiscing elit sed diam nonumy nibh euismod tincidunt ut laoreet dolore magna.Ut wisi enim minim venim quis nostrud exerci.</p>
  <a class="more-link">READ MORE <svg class="arrow" viewBox="0 0 16 10"><path d="M0 5h13M9 1l4 4-4 4" stroke="#1b1b1b" stroke-width="2" fill="none"/></svg></a>
</article>

<article class="service-card" style="left:783px">
  <svg class="service-icon" viewBox="0 0 62 62" fill="none" stroke="#1a84f5" stroke-width="2.2" stroke-linejoin="round" stroke-linecap="round">
    <path d="M6 36l30-24 10 20-36 12z"/><path d="M6 36l4 8"/><path d="M14 42l6 14 6-2-4-13"/>
    <path d="M40 18l4 8"/><path d="M48 8l3-5M54 16l6-2M51 12l5-4"/>
  </svg>
  <h3>MARKETING</h3>
  <p>Lorem ipsum dolor sit consectetuer adipiscing elit sed diam nonumy nibh euismod tincidunt ut laoreet dolore magna.Ut wisi enim minim venim quis nostrud exerci.</p>
  <a class="more-link">READ MORE <svg class="arrow" viewBox="0 0 16 10"><path d="M0 5h13M9 1l4 4-4 4" stroke="#1b1b1b" stroke-width="2" fill="none"/></svg></a>
</article>

<div class="feature-photo" role="img" aria-label="Photo of a scientist in safety glasses pouring blue liquid into test tubes in a lab"></div>
<section class="feature-box">
  <h2>UT WISI ENIM AD MINIM VENIM, QUIS NOSTRUD EXERCI TATION</h2>
  <p>Lorem ipsum dolor sit amet, consectetuer adipiscing elit, sed diam nonummy nibh mod tincidunt ut laoreet dolore magna aliquam erat volutpat. Ut wisi enim ad minim venim, quis nostrud exerci tation ullaorper suscpit lobortis nisl ut aliquip ex ea comodo consat. Duis autem vel eum iriure dolor in hendrerit.</p>
  <a class="more-link">LEARN MORE <svg class="arrow" viewBox="0 0 16 10"><path d="M0 5h13M9 1l4 4-4 4" stroke="#ffffff" stroke-width="2" fill="none"/></svg></a>
</section>

<h2 class="section-title news-title">LATEST <em>NEWS</em></h2>

<article class="news-card" style="left:113px">
  <div class="news-img" role="img" aria-label="Photo of gloved hands pipetting into a sample tray beside lab glassware" style="background:linear-gradient(135deg,#cfe4ee,#3f8fae 55%,#1e5f7e)"></div>
  <p class="news-date">June 15, 2019</p>
  <h3>Lorem ipsum dolor sit a consectetuer adipiscing elit sed diam</h3>
</article>
<article class="news-card" style="left:448px">
  <div class="news-img" role="img" aria-label="Photo of two researchers reviewing data at a lab workstation" style="background:linear-gradient(135deg,#b9c3c9,#8c979d 50%,#d8dde0)"></div>
  <p class="news-date">June 15, 2019</p>
  <h3>Lorem ipsum dolor sit a consectetuer adipiscing elit sed diam</h3>
</article>
<article class="news-card" style="left:783px">
  <div class="news-img" role="img" aria-label="Illustration of a pipette dropping liquid into a glowing molecular pattern" style="background:linear-gradient(135deg,#2b86c7,#7fc4e8 45%,#e9b3c6 60%,#4f9fd3)"></div>
  <p class="news-date">June 15, 2019</p>
  <h3>Lorem ipsum dolor sit a consectetuer adipiscing elit sed diam</h3>
</article>

<a class="btn-outline" style="left:543px;top:2836px;width:113px;height:42px">VIEW ALL</a>

<footer class="site-footer">
  <h4 class="footer-heading" style="left:113px">QUICK LINKS</h4>
  <ul class="quick-links">
    <li>Home</li><li>About us</li><li>Services</li><li>News</li><li>Contact Us</li>
  </ul>

  <h4 class="footer-heading" style="left:304px">CONTACT DETAILS</h4>
  <div class="contact">
    <div class="contact-row" style="top:0">
      <svg viewBox="0 0 13 15"><path d="M6.5 1a5 5 0 0 0-5 5c0 4 5 8.5 5 8.5s5-4.5 5-8.5a5 5 0 0 0-5-5z" fill="#1a84f5"/><circle cx="6.5" cy="6" r="2" fill="#f3f7fd"/></svg>
      <div><strong>CORVENTA DX</strong><br><span style="line-height:18px">123 Lorem ipsum dolor sit amet,<br>consectetuer adipiscing elit.</span></div>
    </div>
    <div class="contact-row" style="top:75px">
      <svg viewBox="0 0 13 15"><path d="M3 1l3 3-1.5 2a8 8 0 0 0 4 4L10.5 8.5l3 3-2 2.5C6 13 1 8 .8 3z" fill="#1a84f5"/></svg>
      <span>(123) 456-7890</span>
    </div>
    <div class="contact-row" style="top:106px">
      <svg viewBox="0 0 13 15"><path d="M1 8l11-6-3 12-3-4z" fill="none" stroke="#1a84f5" stroke-width="1.5" stroke-linejoin="round"/></svg>
      <span>info@corventadx.com</span>
    </div>
  </div>

  <h4 class="footer-heading" style="left:617px">LOCATION MAP</h4>
  <div class="map" role="img" aria-label="Street map showing the office location"></div>

  <div class="footer-brand"><span class="brand-name">Corventa Dx</span></div>

  <div class="footer-rule"></div>
  <p class="copyright">Copyright © 2019 CORVENTA DX. All Rights Reserved.</p>
  <div class="social" aria-label="Social links">
    <span style="background:#3b5998"></span>
    <span style="background:#1da1f2"></span>
    <span style="background:#0e76a8"></span>
    <span style="background:#a0735a"></span>
  </div>
</footer>

</body>
</html>
```